Business Card Designs

Looking to design a 3.5" x 2" standard business card for our employees.
The design needs to be sleek, simple, and modern. We would like our logo (attached) to be incorporated, but not in that colour, rather an outline of the logo in either gold or silver (whichever looks better).

Modern and Simple is what we are looking for, but be creative in incorporating the logo.

```html
<!DOCTYPE html>
<html lang="en">
<head>
<meta charset="utf-8">
<title>Harbourline Suites – Business Card</title>
<link href="https://fonts.googleapis.com/css2?family=Open+Sans:wght@400;600;700&display=swap" rel="stylesheet">
<style>
  :root {
    --backdrop: #d9d8d3;
    --paper: #fbfbf9;
    --gold: #c99a3e;
    --gold-card: #d3a456;
    --gold-deep: #a97c2c;
    --ink: #55524d;
    --shadow: rgba(60, 55, 45, 0.22);
  }
  * { box-sizing: border-box; margin: 0; padding: 0; }
  html, body {
    width: 1200px; height: 801px; overflow: hidden;
    background: var(--backdrop);
    font-family: "Open Sans", Arial, sans-serif;
  }
  .sheet {
    width: 1200px; height: 801px;
    display: flex; align-items: center; justify-content: center; gap: 60px;
  }
  .card {
    width: 500px; height: 286px;
    box-shadow: 0 8px 22px var(--shadow);
    position: relative;
  }
  .card--front {
    background: var(--paper);
    border-bottom: 3px solid var(--gold);
    display: flex; align-items: center;
    padding: 0 36px;
  }
  .brand {
    width: 190px;
    display: flex; flex-direction: column; align-items: center; gap: 14px;
  }
  .brand__mark {
    width: 54px; height: 54px; border: 3px solid var(--gold);
  }
  .brand__name {
    color: var(--gold); font-weight: 600;
    font-size: 15px; letter-spacing: 2.5px; text-transform: uppercase;
    text-align: center; line-height: 1.4;
  }
  .divider {
    width: 1px; height: 150px; background: var(--gold); margin: 0 28px 0 14px;
  }
  .details { color: var(--ink); font-size: 13px; line-height: 1.45; }
  .details__name {
    color: var(--gold); font-weight: 700; font-size: 17px; letter-spacing: 0.5px;
    text-transform: uppercase;
  }
  .details__role { margin-bottom: 12px; }
  .details__address { margin-bottom: 12px; }
  .contact { list-style: none; }
  .contact li { display: flex; align-items: center; gap: 8px; }
  .contact svg { width: 11px; height: 11px; flex: none; fill: var(--gold); }
  .card--back {
    background: var(--gold-card);
    display: flex; flex-direction: column; align-items: center; justify-content: center; gap: 16px;
  }
  .card--back .brand__mark { border-color: var(--gold-deep); width: 70px; height: 70px; }
  .card--back .brand__name { color: var(--gold-deep); font-size: 17px; }
</style>
</head>
<body>
<main class="sheet">
  <section class="card card--front">
    <div class="brand">
      <span class="brand__mark"></span>
      <p class="brand__name">Harbourline Suites</p>
    </div>
    <div class="divider"></div>
    <div class="details">
      <p class="details__name">Daniel Reeve</p>
      <p class="details__role">President</p>
      <p class="details__address">1180 Marina Crest Way<br>Seaview CA 90210</p>
      <ul class="contact">
        <li><svg viewBox="0 0 12 12"><path d="M2 1l2.5 0 1 3-1.5 1a6 6 0 0 0 3 3l1-1.5 3 1V11c-5 0-9-4-9-9z"/></svg>555-014-2087</li>
        <li><svg viewBox="0 0 12 12"><path d="M0 2h12v1.2L6 7 0 3.2zM0 4.6l6 3.8 6-3.8V10H0z"/></svg>hello@harbourlinesuites.com</li>
        <li><svg viewBox="0 0 12 12"><circle cx="6" cy="6" r="5.5"/></svg>www.harbourlinesuites.com</li>
      </ul>
    </div>
  </section>
  <section class="card card--back">
    <span class="brand__mark"></span>
    <p class="brand__name">Harbourline Suites</p>
  </section>
</main>
</body>
</html>
```